Roofing & Siding door hanger flyer

-Looking to make door hanger flyer for Korvell Roofing & Siding
-4.5" wide x 11" tall
-2 sided full colour
-We have started a new website (the content is changing) I have attached photos.
-About us:
-25 year labour warranty's available
-32 years in Calgary
-QHT A+ Member
-NWPC (Prairie Westmark Shingle Council) (logo attached)
-TEK Summit Premier (logo attached)
-Owen Calloway (logo attached)
-Slogan "Raised On Grit, Proven Through Storms" 32 years in Calgary
-Sale
-Page 1 & 2 design ideas
We are in your area, contact us today for your Exclusive limited time offer! *discounts apply exclusively to new agreements only
Updates
-Please keep simple, clean & bright
-I really like the bright blue from our new logo (new logo uploaded)
-We specialize in Roofing -Siding-Gutters & full Exterior Renos (like the competitor example uploaded)
-This is the NEW website we are currently working on (not finished) https://mockups.plenvio.net/view/8b2c4e71-d95a-4f0b-b7e3-c1c1c8823a7f-9d2b/?fullscreen
-This is our OLD website https://northpeakshinglepros.com
-For the sale "We are in your area, contact us today for your Exclusive limited time offer" *discounts apply exclusively to new agreements only
-Free Estimates
-our phone# is 403-555-0187
-our website is northpeakshinglepros.com
-keep simple, clean, bright use the "new logo" uploaded. Check out the competitor example uploaded file
-We are in your area, Contact us today for your Exclusive limited time offer! *discounts apply to new agreements only
-FREE ESTIMATES
-Specialized in Roofing /Siding /Gutters Full Exterior Reno's
-We are currently working on a NEW website https://mockups.plenvio.net/view/8b2c4e71-d95a-4f0b-b7e3-c1c1c8823a7f-9d2b/?fullscreen
-Our OLD website https://northpeakshinglepros.com/
-Post old site address on flyer northpeakshinglepros.com
-Phone # 403-555-0187
Target Market(s)
40-55
Industry/Entity Type
Roofing Siding & full Exterior Reno's
Look and feel

```html
<!DOCTYPE html>
<html lang="en">
<head>
<meta charset="utf-8">
<title>Korvell Roofing &amp; Siding – Door Hanger</title>
<link href="https://fonts.googleapis.com/css2?family=Montserrat:wght@500;600;700;800&family=Poppins:ital,wght@0,600;0,700;0,800;1,800&display=swap" rel="stylesheet">
<style>
  :root{
    --sky-top:#1f6ff6;
    --sky-bottom:#5aa4f7;
    --brand-blue:#2f7cf0;
    --mid-blue:#4a9af4;
    --pale-blue:#eaf3ff;
    --cyan:#8ff3ff;
    --red:#ee1c25;
    --navy:#1d4fb8;
    --ink:#1b1b1b;
    --white:#ffffff;
  }
  html,body{margin:0;padding:0;overflow:hidden;background:#fff;}
  .hanger{
    position:relative;width:1200px;height:2856px;overflow:hidden;
    background:var(--white);
    font-family:"Montserrat",sans-serif;color:var(--ink);
  }
  .hero-sky{
    position:absolute;left:0;top:0;width:1200px;height:1200px;
    background:linear-gradient(180deg,var(--sky-top) 0%,#3f8cf6 30%,var(--sky-bottom) 55%,#8cbcf2 70%);
  }
  .hero-photo{
    position:absolute;left:0;top:500px;width:1200px;height:680px;
    background:
      linear-gradient(180deg,rgba(120,170,240,0) 0%,rgba(160,180,205,.85) 18%,#8e9db3 35%,#6f85a8 60%,#5d7398 82%,#6d7680 100%);
  }
  .area-title{
    position:absolute;left:0;top:100px;width:1200px;text-align:center;
    font-weight:800;font-size:54px;letter-spacing:-0.5px;color:var(--white);margin:0;
  }
  .area-title .accent{color:var(--cyan);}
  .slogan-badge{
    position:absolute;left:92px;top:262px;width:318px;height:300px;
    background:var(--red);border:5px solid var(--white);border-radius:40px;
    box-sizing:border-box;display:flex;align-items:center;justify-content:center;
    text-align:center;
  }
  .slogan-badge p{
    margin:0;font-family:"Poppins",sans-serif;font-style:italic;font-weight:800;
    font-size:38px;line-height:40px;color:var(--white);
  }
  .hero-waves{position:absolute;left:0;top:1060px;width:1200px;height:290px;}
  .brand{
    position:absolute;left:0;top:1432px;width:1200px;text-align:center;
  }
  .brand-est{font-size:24px;font-weight:600;letter-spacing:3px;color:var(--ink);margin:0 0 6px;}
  .brand-name{
    margin:0;font-family:"Montserrat",sans-serif;font-weight:800;color:var(--ink);
    font-size:84px;line-height:86px;letter-spacing:12px;
  }
  .brand-name .sub{display:block;font-weight:500;font-size:40px;line-height:50px;letter-spacing:8px;margin-top:2px;}
  .stat-frame{position:absolute;left:0;top:1630px;width:1200px;height:400px;}
  .stat{position:absolute;top:1628px;text-align:center;}
  .stat-warranty{left:150px;width:400px;}
  .stat-years{left:636px;width:400px;}
  .stat-number{
    display:block;font-weight:800;font-size:210px;line-height:178px;letter-spacing:-8px;
    color:var(--brand-blue);text-shadow:6px 4px 0 var(--cyan);
  }
  .stat-unit{
    display:block;font-weight:800;font-size:74px;line-height:72px;margin-top:-4px;
    color:var(--brand-blue);text-shadow:3px 2px 0 var(--cyan);
  }
  .stat-text{display:block;font-weight:800;font-size:42px;line-height:38px;color:var(--ink);margin-top:6px;}
  .stat-years .stat-text{margin-top:37px;}
  .partners{position:absolute;left:0;top:2055px;width:1200px;height:145px;}
  .contact-title{
    position:absolute;left:0;top:2212px;width:1200px;margin:0;text-align:center;
    font-family:"Poppins",sans-serif;font-weight:800;font-size:110px;line-height:124px;
    letter-spacing:-3px;color:var(--brand-blue);
  }
  .offer{
    position:absolute;left:0;top:2338px;width:1200px;margin:0;text-align:center;
    font-family:"Poppins",sans-serif;font-weight:700;font-size:50px;line-height:60px;color:var(--brand-blue);
  }
  .disclaimer{
    position:absolute;left:0;top:2410px;width:1200px;margin:0;text-align:center;
    font-family:"Poppins",sans-serif;font-weight:600;font-size:31px;color:var(--ink);
  }
  .footer-band{position:absolute;left:0;top:2500px;width:1200px;height:356px;}
  .estimate-pill{
    position:absolute;left:188px;top:2486px;width:826px;height:96px;border-radius:48px;
    background:var(--red);box-shadow:6px 8px 0 var(--navy);
    display:flex;align-items:center;justify-content:center;
    font-weight:800;font-size:78px;color:var(--white);letter-spacing:1px;
  }
  .phone{
    position:absolute;left:0;top:2612px;width:1200px;display:flex;align-items:center;justify-content:center;gap:24px;
    font-weight:800;font-size:112px;line-height:110px;color:var(--white);letter-spacing:-2px;
  }
  .phone svg{width:92px;height:92px;flex:none;}
  .website{
    position:absolute;left:0;top:2718px;width:1200px;margin:0;text-align:center;
    font-family:"Poppins",sans-serif;font-weight:700;font-size:48px;color:var(--white);
  }
</style>
</head>
<body>
<main class="hanger">
  <div class="hero-sky"></div>
  <div class="hero-photo" role="img" aria-label="Photo of a two-storey blue-sided house with a grey shingle roof, white trim and stone base under a clear blue sky"></div>

  <h1 class="area-title">WE’RE IN YOUR <span class="accent">NEIGHBOURHOOD!</span></h1>

  <div class="slogan-badge"><p>Raised<br>On Grit,<br>Proven<br>Through<br>Storms</p></div>

  <svg class="hero-waves" viewBox="0 0 1200 290" preserveAspectRatio="none" aria-hidden="true">
    <defs>
      <radialGradient id="glow" cx="0.8" cy="0.35" r="0.4">
        <stop offset="0" stop-color="#8ff8ff"/>
        <stop offset="1" stop-color="#4a9af4"/>
      </radialGradient>
    </defs>
    <path d="M0 0 C200 120 420 110 640 80 C860 50 1020 20 1200 30 L1200 290 L0 290 Z" fill="#fff"/>
    <path d="M0 30 C150 110 360 130 600 90 C820 55 1000 40 1200 40 L1200 160 C1000 150 800 150 560 190 C320 230 140 210 0 150 Z" fill="url(#glow)"/>
    <path d="M0 20 C160 95 360 120 600 85 C820 55 1000 35 1200 30 L1200 50 C1000 48 820 62 600 100 C360 140 160 120 0 60 Z" fill="#2f7cf0"/>
    <path d="M0 170 C160 235 360 250 600 210 C820 175 1000 165 1200 175 L1200 195 C1000 185 820 195 600 230 C360 270 160 255 0 190 Z" fill="#4a9af4"/>
  </svg>

  <section class="brand">
    <p class="brand-est">Est. 1991</p>
    <p class="brand-name">KORVELL<span class="sub">ROOFING &amp; SIDING</span></p>
  </section>

  <svg class="stat-frame" viewBox="0 0 1200 400" aria-hidden="true">
    <g fill="none" stroke="#4a9af4" stroke-width="4">
      <path d="M584 9 V322 Q584 386 520 386 H146"/>
      <path d="M1059 9 V322 Q1059 386 995 386 H621"/>
    </g>
    <g fill="#4a9af4">
      <circle cx="584" cy="9" r="7"/><circle cx="146" cy="386" r="7"/>
      <circle cx="1059" cy="9" r="7"/><circle cx="621" cy="386" r="7"/>
    </g>
  </svg>

  <div class="stat stat-warranty">
    <span class="stat-number">25</span>
    <span class="stat-unit">YEAR</span>
    <span class="stat-text">LABOUR<br>WARRANTIES<br>AVAILABLE</span>
  </div>
  <div class="stat stat-years">
    <span class="stat-number">32</span>
    <span class="stat-unit">YEARS</span>
    <span class="stat-text">IN CALGARY</span>
  </div>

  <svg class="partners" viewBox="0 0 1200 145" role="img" aria-label="Partner and membership badges: NWPC, QHT A+ rating, TEK Summit Premier, Owen Calloway">
    <g fill="#eaf3ff" stroke="#4a9af4" stroke-width="3">
      <rect x="142" y="14" width="166" height="118" rx="18"/>
      <rect x="364" y="18" width="206" height="114" rx="18"/>
      <rect x="660" y="12" width="116" height="124" rx="18"/>
      <rect x="818" y="18" width="252" height="114" rx="18"/>
    </g>
  </svg>

  <h2 class="contact-title">contact us today</h2>
  <p class="offer">for your Exclusive limited time offer</p>
  <p class="disclaimer">*discounts apply exclusively to new agreements only</p>

  <svg class="footer-band" viewBox="0 0 1200 356" preserveAspectRatio="none" aria-hidden="true">
    <path d="M0 50 C300 10 900 10 1200 50 L1200 356 L0 356 Z" fill="#4a9af4"/>
    <path d="M0 95 C300 45 900 45 1200 95 L1200 356 L0 356 Z" fill="#2f7cf0"/>
  </svg>

  <div class="estimate-pill">FREE ESTIMATES</div>

  <div class="phone">
    <svg viewBox="0 0 92 92" aria-hidden="true">
      <circle cx="46" cy="46" r="46" fill="#fff"/>
      <path d="M33 22 C29 22 24 27 24 33 C24 52 40 68 59 68 C65 68 70 63 70 59 L70 55 L58 49 L52 55 C45 52 40 47 37 40 L43 34 L37 22 Z" fill="#2f7cf0"/>
    </svg>
    <span>403-555-0187</span>
  </div>
  <p class="website">www.northpeakshinglepros.com</p>
</main>
</body>
</html>
```